Mirela Dawn Business Card Design

I need a business card for my daughter. She has it all described in the file below. But it needs to be square in shape. http://www.mireladawn.example is her web site

Target Market(s)

18-35 year old women

Industry/Entity Type

Fashion

Contact Information for Business Card

Please look at the attached file as it has all the details.

Requirements
Must have
• Please look at the attached file as it has all the details.
Nice to have
Should not have

```html
<!DOCTYPE html>
<html lang="en">
<head>
<meta charset="utf-8">
<title>Mirela Dawn – Square Business Card</title>
<link rel="stylesheet" href="https://fonts.googleapis.com/css2?family=Abril+Fatface&family=Satisfy&family=Didact+Gothic&display=swap">
<style>
  :root {
    --backdrop: #2e3142;
    --marble-black: #050505;
    --marble-vein: #6b6b6b;
    --blush: #fbc4c2;
    --ink: #1e1e1e;
    --white: #ffffff;
  }
  * { box-sizing: border-box; margin: 0; padding: 0; }
  html, body {
    width: 1200px;
    height: 840px;
    overflow: hidden;
    background: var(--backdrop);
  }
  .canvas {
    position: relative;
    width: 1200px;
    height: 840px;
  }
  .card {
    position: absolute;
    top: 206px;
    width: 428px;
    height: 426px;
    overflow: hidden;
    box-shadow: 0 10px 24px rgba(0, 0, 0, 0.35);
  }
  .card--front { left: 118px; }
  .card--back { left: 649px; }

  .marble {
    position: absolute;
    inset: 0;
    background:
      radial-gradient(ellipse 60% 35% at 15% 15%, rgba(150,150,150,0.35), transparent 70%),
      radial-gradient(ellipse 40% 30% at 90% 85%, rgba(170,170,170,0.35), transparent 70%),
      radial-gradient(ellipse 50% 25% at 30% 60%, rgba(110,110,110,0.2), transparent 70%),
      var(--marble-black);
  }

  /* Front */
  .brand-name {
    position: absolute;
    left: 0;
    right: 0;
    top: 100px;
    text-align: center;
    font-family: "Abril Fatface", serif;
    font-size: 50px;
    letter-spacing: 1px;
    color: var(--blush);
    text-transform: uppercase;
    line-height: 1;
  }
  .divider {
    position: absolute;
    left: 68px;
    top: 192px;
    width: 290px;
    height: 7px;
    background: var(--white);
  }
  .slogan {
    position: absolute;
    left: 0;
    right: 0;
    top: 240px;
    text-align: center;
    font-family: "Satisfy", cursive;
    font-size: 42px;
    color: var(--blush);
    line-height: 1;
  }

  /* Back */
  .contact-panel {
    position: absolute;
    left: 42px;
    top: 41px;
    width: 343px;
    height: 343px;
    background: var(--blush);
    color: var(--ink);
  }
  .website {
    position: absolute;
    left: 0;
    right: 0;
    top: 14px;
    text-align: center;
    font-family: "Abril Fatface", serif;
    font-size: 31px;
    letter-spacing: 0.5px;
    line-height: 1;
  }
  .topics {
    position: absolute;
    left: 0;
    right: 0;
    top: 62px;
    text-align: center;
    font-family: "Satisfy", cursive;
    font-size: 26px;
    line-height: 1;
  }
  .channels {
    list-style: none;
    position: absolute;
    left: 27px;
    top: 114px;
  }
  .channel {
    display: flex;
    align-items: center;
    height: 42px;
    margin-bottom: 10.5px;
  }
  .channel__dot {
    width: 42px;
    height: 42px;
    border-radius: 50%;
    background: var(--ink);
    flex: none;
  }
  .channel__handle {
    margin-left: 44px;
    font-family: "Didact Gothic", sans-serif;
    font-size: 15.5px;
    white-space: nowrap;
  }
</style>
</head>
<body>
<main class="canvas">
  <section class="card card--front">
    <div class="marble" role="img" aria-label="Black marble texture with white veins"></div>
    <h1 class="brand-name">Mirela Dawn</h1>
    <div class="divider"></div>
    <p class="slogan">fluent in fashion</p>
  </section>

  <section class="card card--back">
    <div class="marble" role="img" aria-label="Black marble texture with white veins"></div>
    <div class="contact-panel">
      <p class="website">mireladawn.example</p>
      <p class="topics">beauty- fashion -travel</p>
      <ul class="channels">
        <li class="channel"><span class="channel__dot"></span><span class="channel__handle">pixgram.example/mireladawnxo</span></li>
        <li class="channel"><span class="channel__dot"></span><span class="channel__handle">chirpline.example/mireladawnxo</span></li>
        <li class="channel"><span class="channel__dot"></span><span class="channel__handle">@mireladawnxo</span></li>
        <li class="channel"><span class="channel__dot"></span><span class="channel__handle">clipcast.example/mireladawn</span></li>
      </ul>
    </div>
  </section>
</main>
</body>
</html>
```